Media Company Needs Homepage Design

We need a homepage design for our studio. Our media company works with a network of on-camera talent and experts to create quality content for the internet. We are targeting top talent in various industries to join our network to star in online video series, write articles, and share their expertise with the world.

We share knowledge with the world and would like our homepage to communicate that. We'd also like for it to appeal to an accomplished audience looking to build their brand and stand out in their industry. Think 'sleek,' 'modern' and 'visual.'

The main message is: 'Create, Engage, Stand Out' and our tagline is: "The Platform for Influential Voices.'

Our secondary message with a call to action:
We offer an innovative way for you to promote yourself to new audiences through original content.
Call to action: Partner with us
Updates

Hi all,

Just a few days left to submit a design. We'd love to see what you come up with! Please message with any questions.

Thank you!

Industry/Entity Type

Internet

Requirements
Must have
• Focus on 'stand out' as primary message in 'create, engage, stand out.' Our target audience is looking for ways to stand out in their industry.
Nice to have
• Could focus on the words 'create, engage, stand out' and play with various type treatments. Words as primary imagery. See attached photo for example.

Could focus on knowledge as primary concept and imagery. example: brainwaves, books, sharing knowledge, knowledge is power.

Could include space for two less prominent sub sections for copy and call-to-action

Could focus on bold, creative imagery. See attached photo for example.

```html
<!DOCTYPE html>
<html lang="en">
<head>
<meta charset="utf-8">
<title>The Platform for Influential Voices</title>
<link rel="stylesheet" href="https://fonts.googleapis.com/css2?family=Quicksand:wght@400;500&family=Open+Sans:wght@400;600&family=Noto+Sans:wght@400;700&display=swap">
<style>
  :root {
    --pink: #ef6f90;
    --pink-light: #f07a98;
    --hero-top: #e9688a;
    --hero-bottom: #d24a72;
    --wine: #9d1c3c;
    --wine-bump: #a8214a;
    --ring: #e0557c;
    --ink: #2a1a20;
    --white: #ffffff;
    --cream: #fde8e6;
    --button-top: #eef2f8;
    --button-bottom: #a9b8d0;
    --button-ink: #25304a;
    --arrow: #d43a55;
  }
  * { margin: 0; padding: 0; box-sizing: border-box; }
  html, body { width: 1200px; height: 1200px; overflow: hidden; background: var(--pink); }
  .page { position: relative; width: 1200px; height: 1200px; overflow: hidden; font-family: "Noto Sans", Verdana, sans-serif; }

  .site-header { position: absolute; left: 0; top: 0; width: 1200px; height: 64px; background: var(--pink-light); border-bottom: 1px solid #c94a6c; }
  .site-title { position: absolute; left: 43px; top: 10px; font-family: "Open Sans", sans-serif; font-weight: 400; font-size: 37px; color: var(--white); }
  .site-nav { position: absolute; right: 72px; top: 30px; font-family: "Noto Sans", sans-serif; font-weight: 700; font-size: 16px; color: var(--ink); word-spacing: 4px; }

  .hero { position: absolute; left: 0; top: 64px; width: 1200px; height: 480px; background: radial-gradient(ellipse at 75% 30%, #f07a9a 0%, var(--hero-top) 35%, var(--hero-bottom) 100%); }
  .hero-title { position: absolute; left: 44px; top: 44px; width: 646px; font-family: "Quicksand", sans-serif; font-weight: 400; font-size: 58px; line-height: 62px; color: var(--white); text-align: justify; text-align-last: left; letter-spacing: 2px; text-shadow: 0 1px 2px rgba(80,0,30,.4); }
  .hero-title .first-line { display: block; text-align-last: justify; }
  .hero-copy { position: absolute; left: 45px; top: 173px; width: 627px; font-weight: 700; font-size: 16.5px; line-height: 20px; color: var(--ink); text-align: justify; letter-spacing: .6px; }
  .cta-button { position: absolute; left: 47px; top: 267px; width: 320px; height: 67px; border-radius: 7px; border: 2px solid #f3f5fa; background: linear-gradient(var(--button-top), var(--button-bottom)); box-shadow: 0 3px 5px rgba(60,0,20,.45); display: flex; align-items: center; padding-left: 32px; font-family: "Open Sans", sans-serif; font-size: 22px; font-weight: 400; color: var(--button-ink); letter-spacing: 1px; text-decoration: none; }
  .cta-button svg { position: absolute; right: 20px; top: 22px; }
  .hero-visual { position: absolute; left: 760px; top: 23px; width: 347px; height: 453px; border-radius: 40px; background: radial-gradient(ellipse at 60% 45%, #c8c8cc 0%, #6a6a72 45%, rgba(120,30,60,.5) 75%, rgba(210,74,114,0) 100%); }

  .features { position: absolute; left: 0; top: 544px; width: 1200px; height: 423px; background: var(--wine); }
  .bumps { position: absolute; left: 0; top: 460px; }
  .feature-image { position: absolute; width: 208px; height: 208px; border-radius: 50%; border: 6px solid var(--ring); }
  .img-create { left: 68px; top: 499px; background: radial-gradient(circle at 40% 50%, #f4e8f0, #d8c4e0 60%, #b7d6ee); }
  .img-engage { left: 377px; top: 499px; background: radial-gradient(circle at 50% 50%, #ffffff, #f4eef2 55%, #e6dde4); }
  .img-standout { left: 688px; top: 499px; background: radial-gradient(circle at 50% 60%, #f2c230 0%, #d9d9dc 30%, #c3c3c8 100%); }
  .feature { position: absolute; top: 732px; width: 250px; }
  .feature-create { left: 98px; }
  .feature-engage { left: 396px; top: 735px; }
  .feature-standout { left: 702px; top: 735px; }
  .feature h2 { font-family: "Quicksand", sans-serif; font-weight: 400; font-size: 43px; line-height: 50px; color: var(--cream); letter-spacing: 1.5px; text-shadow: 0 1px 2px rgba(60,0,20,.5); }
  .feature p { margin-top: 12px; font-size: 16px; line-height: 20px; color: var(--white); text-align: justify; text-align-last: left; }

  .site-footer { position: absolute; left: 0; top: 967px; width: 1200px; height: 233px; background: var(--pink); }
  .footer-heading { position: absolute; top: 20px; font-family: "Open Sans", sans-serif; font-weight: 400; font-size: 31px; color: var(--ink); }
  .contact-heading { left: 89px; }
  .follow-heading { left: 488px; }
  .address { position: absolute; left: 93px; top: 76px; width: 256px; font-family: "Open Sans", sans-serif; font-size: 16px; line-height: 20px; color: var(--ink); text-align: justify; text-align-last: left; font-style: normal; }
  .social { position: absolute; left: 492px; top: 78px; display: flex; gap: 22px; }
  .social a { display: flex; align-items: center; gap: 7px; font-family: "Open Sans", sans-serif; font-size: 16px; color: var(--wine); text-decoration: none; }
  .social a::before { content: ""; width: 26px; height: 26px; border-radius: 50%; background: var(--wine); }
  .copyright { position: absolute; right: 33px; top: 205px; font-weight: 700; font-size: 14px; color: var(--ink); }
</style>
</head>
<body>
<div class="page">
  <header class="site-header">
    <div class="site-title">Title</div>
    <nav class="site-nav">link1 &nbsp;| &nbsp;link 2 &nbsp;| &nbsp;link3 &nbsp;| &nbsp;link4</nav>
  </header>

  <section class="hero">
    <h1 class="hero-title"><span class="first-line">The Platform for</span>Influential voices</h1>
    <p class="hero-copy">Porta fusce varius natoque penatibus magnis. Montes nascetr mugiat suada odio. Porta fusce varius natoque penatibus magnis. Montes nascetr mugiat suada odio.</p>
    <a class="cta-button" href="#">PARTNER WITH US
      <svg width="24" height="24" viewBox="0 0 24 24"><circle cx="12" cy="12" r="11" fill="#f4f6fa"/><path d="M8 6 L18 12 L8 18 Z" fill="var(--arrow)"/></svg>
    </a>
    <div class="hero-visual" role="img" aria-label="Studio microphone with headphones over swirling decorations"></div>
  </section>

  <section class="features">
  </section>
  <svg class="bumps" width="1200" height="90" viewBox="0 0 1200 90">
    <path d="M45 84 A127 127 0 0 1 299 84 Z" fill="var(--wine-bump)"/>
    <path d="M354 84 A127 127 0 0 1 608 84 Z" fill="var(--wine-bump)"/>
    <path d="M665 84 A127 127 0 0 1 919 84 Z" fill="var(--wine-bump)"/>
  </svg>
  <div class="feature-image img-create" role="img" aria-label="Hand drawing a rainbow of colours with a pencil"></div>
  <div class="feature-image img-engage" role="img" aria-label="Colourful painted handprints"></div>
  <div class="feature-image img-standout" role="img" aria-label="A bright yellow cube standing out among grey cubes"></div>

  <article class="feature feature-create">
    <h2>CREATE</h2>
    <p>Porta fusce varium natoque penatibus magnis. Montes nascetr mugiat suada odio. Porta fusce varium natoque penatibus magnis. Montes nascetr mugiat suada odio.</p>
  </article>
  <article class="feature feature-engage">
    <h2>ENGAGE</h2>
    <p>Porta fusce varium natoque penatibus magnis. Montes nascetr mugiat suada odio. Porta fusce varium natoque penatibus magnis. Montes nascetr mugiat suada odio.</p>
  </article>
  <article class="feature feature-standout">
    <h2>STANDOUT</h2>
    <p>Porta fusce varium natoque penatibus magnis. Montes nascetr mugiat suada odio. Porta fusce varium natoque penatibus magnis. Montes nascetr mugiat suada odio.</p>
  </article>

  <footer class="site-footer">
    <h3 class="footer-heading contact-heading">Contact Us</h3>
    <address class="address">Address ,Address, Address, Address, Address<br>Address ,Address, Address, Address, Address</address>
    <h3 class="footer-heading follow-heading">Follow us</h3>
    <div class="social">
      <a href="#">Chirper</a>
      <a href="#">FaceLink</a>
    </div>
    <p class="copyright">Copyright 2012. all rights reserved</p>
  </footer>
</div>
</body>
</html>
```